Webdesign für Gravierwerkstatt
Zielgruppe
Das Unternehmen ist eine Gravierwerkstatt - die Zielgruppe sind sowohl private als auch gewerbliche Kunden und Vereine für Einzelauftrgäge oder Kleinserien für Gravuren
Aufgabenstellung
- modernes Layout
- Farbgebung blau, hellblau, Grau, weiß
- übersichtliche Darstellung der angebotenen Leistungen
- kein Kontaktformular
- nicht zu viele Bilder
- es existiert kein richtiges Logo, (es kann aber das Handwerkszeichen wiederverwendet werden)
- Names des Unternehmens 'Gravierwerkstatt Brenner'
- Meisterwerkstatt

```html
<!DOCTYPE html>
<html lang="de">
<head>
<meta charset="utf-8">
<title>Gravierwerkstatt Brenner – Meisterwerkstatt seit 1962</title>
<link rel="stylesheet" href="https://fonts.googleapis.com/css2?family=Inter:wght@400;500;600;700&display=swap">
<style>
:root{
  --navy:#16223a;
  --navy-card:#1f2c45;
  --blue:#0f4a82;
  --blue-soft:#eaf2fb;
  --sky:#f2f7fc;
  --ink:#16223a;
  --text:#4a5568;
  --muted:#6b7686;
  --line:#e6ebf1;
  --white:#ffffff;
}
*{box-sizing:border-box;margin:0;padding:0}
html,body{width:1200px;height:2532px;overflow:hidden}
body{font-family:"Inter",sans-serif;color:var(--ink);background:var(--white);font-size:11px}
.wrap{width:658px;margin:0 auto;position:relative}
.eyebrow{font-size:7px;font-weight:700;letter-spacing:2.2px;color:var(--blue);text-transform:uppercase}
h2{font-weight:500;font-size:30px;line-height:1;letter-spacing:-.5px;margin-top:6px}

/* header */
.site-header{height:42px;border-bottom:1px solid var(--line);background:var(--white)}
.site-header .wrap{display:flex;align-items:center;height:42px}
.brand{display:flex;align-items:center;gap:7px}
.brand-mark{width:20px;height:20px;border-radius:6px;background:var(--blue)}
.brand-name{font-size:8.5px;font-weight:600;line-height:1.1}
.brand-sub{font-size:5.5px;color:var(--muted)}
.nav{display:flex;gap:15px;margin-left:146px;font-size:6.5px;font-weight:600}
.phone-pill{margin-left:auto;background:var(--navy);color:#fff;font-size:7px;font-weight:700;padding:6px 9px;border-radius:12px}

/* hero */
.hero{height:430px;background:linear-gradient(180deg,#f1f6fc,#fff)}
.hero .wrap{display:flex;padding-top:51px}
.hero-copy{width:340px;padding-top:33px}
.tag{display:inline-block;font-size:6px;font-weight:600;color:var(--blue);border:1px solid var(--line);background:#fff;border-radius:10px;padding:4px 7px}
.hero h1{font-size:32px;font-weight:500;line-height:1.05;letter-spacing:-.6px;margin-top:8px}
.hero p{font-size:8px;line-height:1.8;color:var(--text);margin-top:15px;width:300px}
.btns{display:flex;gap:8px;margin-top:17px}
.btn{font-size:7px;font-weight:600;padding:9px 13px;border-radius:14px}
.btn-primary{background:var(--blue);color:#fff}
.btn-ghost{border:1px solid var(--line);background:#fff}
.hero-media{margin-left:auto;width:298px;height:318px;border-radius:18px;position:relative;
  background:radial-gradient(circle at 50% 40%,#5d5d5c,#3a3a39 70%,#2a2a29);box-shadow:0 16px 30px rgba(22,34,58,.18)}
.hero-badge{position:absolute;left:15px;right:15px;bottom:15px;background:rgba(255,255,255,.94);border-radius:10px;padding:9px 12px}
.hero-badge small{display:block;font-size:6px;font-weight:700;color:var(--blue)}
.hero-badge strong{font-size:11px;font-weight:500}

/* services */
.services{height:282px;padding-top:42px}
.services .head{display:flex;justify-content:space-between;align-items:flex-end}
.services .head p{width:270px;font-size:7px;line-height:1.6;color:var(--text);margin-bottom:2px}
.cards{display:flex;gap:11px;margin-top:26px}
.card{flex:1;height:121px;border:1px solid var(--line);border-radius:12px;padding:16px 15px;box-shadow:0 2px 6px rgba(22,34,58,.04)}
.icon-box{width:25px;height:25px;border-radius:7px;background:var(--blue-soft);display:flex;align-items:center;justify-content:center}
.card h3{font-size:11px;font-weight:600;margin-top:15px}
.card p{font-size:7px;line-height:1.85;color:var(--text);margin-top:8px}

/* engraving */
.engraving{height:472px;background:var(--navy);color:#fff;padding-top:54px}
.engraving .eyebrow{color:#8fb6e6}
.engraving h2{font-size:28px;line-height:1.02}
.eng-cards{display:flex;gap:11px;margin-top:26px}
.eng-card{flex:1;height:268px;background:var(--navy-card);border:1px solid #2c3a55;border-radius:12px;overflow:hidden}
.eng-photo{height:103px}
.eng-body{padding:15px 15px}
.eng-body h3{font-size:11px;font-weight:600}
.eng-body ul{list-style:none;margin-top:12px}
.eng-body li{font-size:7px;line-height:1.55;color:#c9d3e2;padding-left:9px;position:relative;margin-bottom:4px}
.eng-body li::before{content:"";position:absolute;left:0;top:4px;width:3px;height:3px;border-radius:50%;background:#8fb6e6}

/* about */
.about{height:367px;padding-top:52px}
.about .wrap{display:flex;gap:26px}
.about-photo{width:316px;height:262px;border-radius:16px;background:radial-gradient(circle at 40% 45%,#c48a4a,#4a3a32 55%,#1e2a3a)}
.about-copy{flex:1;padding-top:25px}
.about-copy h2{line-height:1}
.about-copy p{font-size:7.7px;line-height:1.95;color:var(--text);margin-top:20px}
.stats{display:flex;gap:8px;margin-top:20px}
.stat{flex:1;background:var(--sky);border-radius:10px;padding:11px 12px;height:50px}
.stat b{display:block;font-size:14px;font-weight:500;color:var(--blue)}
.stat span{font-size:6px;color:var(--muted)}

/* contact */
.contact{height:375px;background:var(--sky);padding-top:52px}
.contact-grid{display:flex;gap:12px;margin-top:20px}
.address-card{width:348px;height:202px;background:#fff;border-radius:14px;padding:19px 19px}
.address-card h3{font-size:11px;font-weight:500}
.address-card .owner{font-size:6.5px;color:var(--muted);margin-top:4px}
.info-grid{display:grid;grid-template-columns:1fr 1fr;gap:16px 10px;margin-top:18px}
.info{display:flex;gap:9px}
.info-icon{width:20px;height:20px;border-radius:50%;background:var(--blue-soft);display:flex;align-items:center;justify-content:center;flex:none}
.info b{display:block;font-size:7px;font-weight:600}
.info span{font-size:7px;line-height:1.55;color:var(--text)}
.route{display:inline-block;margin-top:18px;background:var(--blue);color:#fff;font-size:7px;font-weight:600;padding:8px 11px;border-radius:13px}
.hours{flex:1;height:202px;background:var(--navy);color:#fff;border-radius:14px;padding:19px 19px}
.hours h3{font-size:11px;font-weight:600;margin-bottom:10px}
.hours-row{display:flex;justify-content:space-between;font-size:7px;padding:8px 0;border-bottom:1px solid #2f3d58}
.hours-row:last-child{border-bottom:0}
.hours-row b{font-weight:700}

/* map */
.directions{height:479px;padding-top:52px}
.map{margin-top:20px;height:306px;border-radius:14px;background:linear-gradient(135deg,#dff3e4 0%,#eef1f4 40%,#f1f2f4 100%);position:relative}

/* footer */
.site-footer{height:85px;background:var(--navy);color:#fff;padding-top:28px}
.site-footer .wrap{display:flex;justify-content:space-between}
.site-footer b{font-size:8.5px;font-weight:600}
.site-footer p{font-size:6.5px;color:#aab6c8;margin-top:4px}
.legal{display:flex;gap:11px;font-size:6.5px;color:#d0d8e4}
</style>
</head>
<body>
<header class="site-header">
  <div class="wrap">
    <div class="brand">
      <div class="brand-mark"></div>
      <div><div class="brand-name">Gravierwerkstatt Brenner</div><div class="brand-sub">Meisterwerkstatt seit 1962</div></div>
    </div>
    <nav class="nav"><span>Leistungen</span><span>Gravuren</span><span>Unternehmen</span><span>Kontakt</span></nav>
    <div class="phone-pill">0371 / 40 21 58</div>
  </div>
</header>

<section class="hero">
  <div class="wrap">
    <div class="hero-copy">
      <span class="tag">Gravuren · Schilder · Stempel · Sportpokale · Zinnwaren</span>
      <h1>Präzise Gravuren für Industrie, Vereine und persönliche Stücke.</h1>
      <p>Moderne Meisterwerkstatt in Chemnitz für Schilder, Industriegravuren, Lasergravuren, Handgravuren, Pokale, Vereinsbedarf und Stempel.</p>
      <div class="btns"><span class="btn btn-primary">Kontakt aufnehmen</span><span class="btn btn-ghost">Leistungen ansehen</span></div>
    </div>
    <div class="hero-media" role="img" aria-label="Gegossenes Metallschild der Werkstatt mit Namen und Meisterwerkstatt-Schriftzug">
      <div class="hero-badge"><small>Meisterwerkstatt</small><strong>Seit 1962 in Chemnitz</strong></div>
    </div>
  </div>
</section>

<section class="services">
  <div class="wrap">
    <div class="head">
      <div><div class="eyebrow">Leistungsübersicht</div><h2>Alles klar sichtbar.</h2></div>
      <p>Übersichtliche Darstellung der wichtigsten Leistungen — modern, klar und ohne überladene Inhalte.</p>
    </div>
    <div class="cards">
      <div class="card">
        <div class="icon-box"><svg width="10" height="10" viewBox="0 0 10 10" fill="none" stroke="#0f4a82" stroke-width="1"><circle cx="5" cy="3.5" r="2.4"/><path d="M3.5 5.6 3 9l2-1 2 1-.5-3.4"/></svg></div>
        <h3>Pokale &amp; Vereinsbedarf</h3>
        <p>Pokale, Ehrenpreise, Medaillen, Urkunden sowie Vereinsbedarf für Sportschützen und Feuerwehr.</p>
      </div>
      <div class="card">
        <div class="icon-box"><svg width="10" height="10" viewBox="0 0 10 10" fill="none" stroke="#0f4a82" stroke-width="1"><path d="M6 1v3M4.5 2.5h3M2 4v4M0.5 6h3M7 6l1 1"/></svg></div>
        <h3>Kunsthandwerkliches Zinn</h3>
        <p>Teller, Bierkrüge, Zinnuhren, Leuchter, Becher und Vasen.</p>
      </div>
      <div class="card">
        <div class="icon-box"><svg width="10" height="10" viewBox="0 0 10 10" fill="none" stroke="#0f4a82" stroke-width="1"><circle cx="5" cy="2.5" r="1.5"/><path d="M5 4v2M1.5 6h7v2h-7z"/></svg></div>
        <h3>Stempel</h3>
        <p>Gummistempel, Stahlstempel, Messingstempel, Blindprägestempel, Brennstempel und Petschafte.</p>
      </div>
    </div>
  </div>
</section>

<section class="engraving">
  <div class="wrap">
    <div class="eyebrow">Gravuren</div>
    <h2>Von Industriegravur bis<br>persönlichem Monogramm.</h2>
    <div class="eng-cards">
      <div class="eng-card">
        <div class="eng-photo" role="img" aria-label="Graviertes Messing-Gedenkschild" style="background:linear-gradient(135deg,#8a7a5c,#5e4e36)"></div>
        <div class="eng-body"><h3>Schilder &amp; Industriegravuren</h3>
          <ul><li>Praxis- und Firmenschilder</li><li>Hinweisschilder aus Aluminium, Acrylglas oder Messing</li><li>Türschilder in verschiedenen Formen</li><li>Typenschilder &amp; Bezeichnungsschilder</li><li>Hausnummern</li><li>Bedienblenden und Frontplatten</li></ul></div>
      </div>
      <div class="eng-card">
        <div class="eng-photo" role="img" aria-label="Lasergravierte Buchseite mit Text und Zeichnung" style="background:linear-gradient(135deg,#6b645a,#cfc9bf 50%,#3d3a36)"></div>
        <div class="eng-body"><h3>Lasergravuren</h3>
          <ul><li>Typenschilder und industrielle Kennzeichnungen</li><li>Schreibgeräte</li><li>Individuelle Geschenke</li><li>Gläser</li><li>Gravuren auf Kunststoff, Holz, Glas oder Edelstahl</li></ul></div>
      </div>
      <div class="eng-card">
        <div class="eng-photo" role="img" aria-label="Handgravierte Platten und Schmuckstücke in einer Vitrine" style="background:linear-gradient(135deg,#9a5a34,#b9b2a6 50%,#7a4a2a)"></div>
        <div class="eng-body"><h3>Handgravuren</h3>
          <ul><li>Trauringgravuren</li><li>Monogramme in Gold, Silber und Zinn</li><li>Schmuck, Uhren und persönliche Erinnerungsstücke</li><li>Individuelle Geschenke</li></ul></div>
      </div>
    </div>
  </div>
</section>

<section class="about">
  <div class="wrap">
    <div class="about-photo" role="img" aria-label="Funkenflug bei der Metallbearbeitung in der Werkstatt"></div>
    <div class="about-copy">
      <div class="eyebrow">Wir über uns</div>
      <h2>Handwerk mit<br>Geschichte.</h2>
      <p>Die Gravierwerkstatt wurde 1962 von Graveurmeister Werner Brenner gegründet. Im Jahr 1988 legte Karin Lehmann die Meisterprüfung ab und übernahm den Betrieb im Jahr 2000. 2012 feierte das Unternehmen sein 50-jähriges Jubiläum.</p>
      <div class="stats">
        <div class="stat"><b>1962</b><span>gegründet</span></div>
        <div class="stat"><b>2000</b><span>Übernahme</span></div>
        <div class="stat"><b>7</b><span>ausgebildete Lehrlinge</span></div>
      </div>
    </div>
  </div>
</section>

<section class="contact">
  <div class="wrap">
    <div class="eyebrow">Kontakt</div>
    <h2>Kontakt &amp; Anfahrt</h2>
    <div class="contact-grid">
      <div class="address-card">
        <h3>Gravierwerkstatt Brenner</h3>
        <div class="owner">Inhaberin Graveurmeisterin Karin Lehmann</div>
        <div class="info-grid">
          <div class="info"><div class="info-icon"><svg width="8" height="8" viewBox="0 0 8 8" fill="none" stroke="#0f4a82" stroke-width=".8"><path d="M4 7.5S1.5 5 1.5 3a2.5 2.5 0 0 1 5 0C6.5 5 4 7.5 4 7.5z"/><circle cx="4" cy="3" r=".9"/></svg></div><div><b>Adresse</b><span>Lindenauer Straße 112, 09116<br>Chemnitz</span></div></div>
          <div class="info"><div class="info-icon"><svg width="8" height="8" viewBox="0 0 8 8" fill="none" stroke="#0f4a82" stroke-width=".8"><path d="M1.5 1h1.5l.7 1.7-.9.6a4 4 0 0 0 1.9 1.9l.6-.9L7 5v1.5A.8.8 0 0 1 6.2 7 5.5 5.5 0 0 1 1 1.8.8.8 0 0 1 1.5 1z"/></svg></div><div><b>Telefon</b><span>0371 / 40 21 58</span></div></div>
          <div class="info"><div class="info-icon"><svg width="8" height="8" viewBox="0 0 8 8" fill="none" stroke="#0f4a82" stroke-width=".8"><rect x="1" y="1.8" width="6" height="4.4" rx=".6"/><path d="M1 2.2 4 4.5l3-2.3"/></svg></div><div><b>E-Mail</b><span>info@graveur-brenner.de</span></div></div>
          <div class="info"><div class="info-icon"><svg width="8" height="8" viewBox="0 0 8 8" fill="none" stroke="#0f4a82" stroke-width=".8"><circle cx="4" cy="4" r="3"/><path d="M4 2.3V4l1.2.8"/></svg></div><div><b>Fax</b><span>0371 / 4 02 15 99</span></div></div>
        </div>
        <span class="route">Route öffnen ↗</span>
      </div>
      <div class="hours">
        <h3>Öffnungszeiten</h3>
        <div class="hours-row"><span>Montag</span><b>8–12 Uhr</b></div>
        <div class="hours-row"><span>Dienstag</span><b>8–12 und 14–16 Uhr</b></div>
        <div class="hours-row"><span>Mittwoch</span><b>8–12 und 14–16 Uhr</b></div>
        <div class="hours-row"><span>Donnerstag</span><b>8–12 und 14–18 Uhr</b></div>
        <div class="hours-row"><span>Freitag</span><b>8–12 und 14–18 Uhr</b></div>
      </div>
    </div>
  </div>
</section>

<section class="directions">
  <div class="wrap">
    <div class="eyebrow">Anfahrt</div>
    <h2>So finden Sie uns.</h2>
    <div class="map" role="img" aria-label="Stadtplan mit dem Standort der Werkstatt in Chemnitz"></div>
  </div>
</section>

<footer class="site-footer">
  <div class="wrap">
    <div><b>Gravierwerkstatt Brenner</b><p>Meisterwerkstatt für Gravuren in Chemnitz</p></div>
    <div class="legal"><span>Impressum</span><span>Datenschutzerklärung</span><span>Erklärung zur Barrierefreiheit</span></div>
  </div>
</footer>
</body>
</html>
```